Business card design needed

I am a free lance management consultant looking to have some professionally designed business cards created.
If possible if i could have some bullet points or something with a list of my services that would be great.
Services are:
- Strategic Planning
- Process Improvement
- Change Management
- IT Solutions & Implementation
- IT Consulting
- Web Solutions
Target Market(s)
Business Owners and Operators
Industry/Entity Type
Business
Contact Information for Business Card
Colin Hartley
CH Consulting
0456 318 240
COLIN@COLINHARTLEY.CO
www.colinhartley.co
Logo Text
CH Consulting
Logo styles of interest
Pictorial/Combination Logo
Wordmark Logo
Lettermark Logo

```html
<!DOCTYPE html>
<html lang="en">
<head>
<meta charset="utf-8">
<title>CH Consulting — Business Card</title>
<link rel="stylesheet" href="https://fonts.googleapis.com/css2?family=Source+Sans+3:wght@400;600;700&display=swap">
<style>
  :root {
    --backdrop: #e4e4e4;
    --card: #3b3b3b;
    --green: #6cc04a;
    --white: #ffffff;
    --card-w: 300px;
    --card-h: 525px;
  }
  * { box-sizing: border-box; margin: 0; padding: 0; }
  html, body {
    width: 1200px;
    height: 750px;
    overflow: hidden;
    background: var(--backdrop);
    font-family: "Source Sans 3", "Myriad Pro", Arial, sans-serif;
  }
  .stage {
    position: relative;
    width: 1200px;
    height: 750px;
  }
  .card {
    position: absolute;
    top: 112px;
    width: var(--card-w);
    height: var(--card-h);
    background: var(--card);
    box-shadow: 0 6px 18px rgba(0,0,0,0.25);
    overflow: hidden;
  }
  .card--front { left: 270px; }
  .card--back { left: 630px; }

  /* Front */
  .brand {
    position: absolute;
    top: 92px;
    left: 0;
    right: 0;
    display: flex;
    align-items: center;
    justify-content: center;
    gap: 8px;
  }
  .brand__name {
    color: var(--white);
    font-weight: 700;
    font-size: 26px;
    letter-spacing: 0.5px;
  }
  .brand__dot {
    width: 14px;
    height: 14px;
    border-radius: 50%;
    background: var(--green);
  }
  .holder {
    position: absolute;
    top: 262px;
    left: 48px;
    color: var(--green);
    font-size: 19px;
    font-weight: 400;
    letter-spacing: 0.5px;
  }
  .contacts {
    position: absolute;
    top: 320px;
    left: 26px;
    right: 18px;
    list-style: none;
  }
  .contact {
    display: flex;
    align-items: center;
    height: 44px;
  }
  .contact__icon {
    width: 28px;
    height: 24px;
    flex: none;
  }
  .contact__text {
    flex: 1;
    text-align: center;
    color: var(--white);
    font-size: 15px;
    letter-spacing: 0.4px;
  }
  .contact__text--web { font-size: 17px; letter-spacing: 0.2px; }

  /* Back */
  .services {
    position: absolute;
    top: 80px;
    left: 0;
    list-style: none;
  }
  .service {
    display: table;
    background: var(--green);
    color: var(--white);
    font-size: 18px;
    font-weight: 400;
    line-height: 32px;
    padding: 0 10px 0 14px;
    margin-bottom: 13px;
    white-space: nowrap;
  }
  .card-dots {
    position: absolute;
    bottom: 70px;
    left: 0;
    right: 0;
    display: flex;
    justify-content: center;
    gap: 48px;
  }
  .card-dots span {
    width: 14px;
    height: 14px;
    border-radius: 50%;
    background: var(--green);
  }
</style>
</head>
<body>
<main class="stage">

  <section class="card card--front" aria-label="Business card front">
    <div class="brand">
      <span class="brand__name">CH CONSULTING</span>
      <span class="brand__dot" aria-hidden="true"></span>
    </div>

    <p class="holder">COLIN HARTLEY</p>

    <ul class="contacts">
      <li class="contact">
        <svg class="contact__icon" viewBox="0 0 28 24" aria-hidden="true">
          <path d="M9 3 h4 l1 5 -3 2 c1 3 3 5 6 6 l2 -3 5 1 v4 c0 2 -1 3 -3 3 C11 21 5 14 6 5 c0 -1 1 -2 3 -2z" fill="var(--green)"/>
        </svg>
        <span class="contact__text">0456 318 240</span>
      </li>
      <li class="contact">
        <svg class="contact__icon" viewBox="0 0 28 24" aria-hidden="true">
          <rect x="2" y="5" width="24" height="15" fill="var(--green)"/>
          <path d="M2 5 L14 14 L26 5" fill="none" stroke="var(--card)" stroke-width="1.6"/>
        </svg>
        <span class="contact__text">COLIN@COLINHARTLEY.CO</span>
      </li>
      <li class="contact">
        <svg class="contact__icon" viewBox="0 0 28 24" aria-hidden="true">
          <circle cx="13" cy="12" r="10" fill="var(--green)"/>
          <g fill="none" stroke="var(--card)" stroke-width="1.5">
            <ellipse cx="13" cy="12" rx="4.5" ry="10"/>
            <line x1="3" y1="12" x2="23" y2="12"/>
          </g>
        </svg>
        <span class="contact__text contact__text--web">www.colinhartley.co</span>
      </li>
    </ul>
  </section>

  <section class="card card--back" aria-label="Business card back">
    <ul class="services">
      <li class="service">Strategic Planning</li>
      <li class="service">Process Improvement</li>
      <li class="service">Change Management</li>
      <li class="service">IT Solutions &amp; Implementation</li>
      <li class="service">IT Consulting</li>
      <li class="service">Web Solutions</li>
    </ul>
    <div class="card-dots" aria-hidden="true">
      <span></span><span></span><span></span>
    </div>
  </section>

</main>
</body>
</html>
```